Yoga and Wellness Center

New business- have the logo already, but wanted my cards to be more colorful.

Please find my attached logo. I am only waiting on confirmation of my
telephone number in order to have all the information right. This is for a
new yoga and wellness center in TN for a conservative audience, but I would
like a colorful business card.

Industry/Entity Type

Conservative

```html
<!DOCTYPE html>
<html lang="en">
<head>
<meta charset="utf-8">
<title>Cedar Hollow Yoga – Business Card</title>
<link rel="stylesheet" href="https://fonts.googleapis.com/css2?family=Nunito+Sans:wght@600&family=Arimo:wght@700&display=swap">
<style>
  :root {
    --sky: #ecebf3;
    --ridge: #c2c0da;
    --ridge-deep: #aeacce;
    --sun-glow: #fde9dc;
    --sun: #f6a678;
    --wordmark: #5d5d96;
    --ink: #28347a;
  }
  * { margin: 0; padding: 0; box-sizing: border-box; }
  html, body {
    width: 1200px;
    height: 703px;
    overflow: hidden;
    background: var(--sky);
  }
  .card {
    position: relative;
    width: 1200px;
    height: 703px;
    overflow: hidden;
    background: var(--sky);
  }
  .card__scene {
    position: absolute;
    inset: 0;
    background:
      radial-gradient(circle at 30% 50%, var(--sun-glow) 0%, var(--sun) 40%, rgba(246,166,120,0) 58%),
      linear-gradient(to bottom, var(--sky) 0%, var(--ridge) 55%, var(--ridge-deep) 100%);
  }
  .wordmark {
    position: absolute;
    left: 0;
    right: 0;
    text-align: center;
    white-space: nowrap;
    font-family: "Nunito Sans", "Avenir", sans-serif;
    font-weight: 600;
    color: var(--wordmark);
    line-height: 1;
  }
  .wordmark__primary {
    top: 96px;
    font-size: 100px;
    letter-spacing: 0.2em;
    padding-left: 0.2em;
  }
  .wordmark__secondary {
    top: 226px;
    font-size: 84px;
    letter-spacing: 0.34em;
    padding-left: 0.34em;
  }
  .contact {
    position: absolute;
    right: 42px;
    top: 458px;
    text-align: right;
    white-space: nowrap;
    font-family: "Arimo", Arial, sans-serif;
    font-weight: 700;
    color: var(--ink);
    line-height: 1;
  }
  .contact__name  { font-size: 57px; margin-bottom: 19px; }
  .contact__phone { font-size: 50px; margin-bottom: 16px; }
  .contact__email { font-size: 50px; }
</style>
</head>
<body>
  <div class="card">
    <div class="card__scene" role="img" aria-label="Illustration of a setting sun behind layered lavender mountain ridges"></div>

    <div class="wordmark wordmark__primary">CEDAR HOLLOW</div>
    <div class="wordmark wordmark__secondary">YOGA</div>

    <div class="contact">
      <p class="contact__name">Dan Hartley</p>
      <p class="contact__phone">1.800.555.0147</p>
      <p class="contact__email">Dan@CedarHollowYoga.com</p>
    </div>
  </div>
</body>
</html>
```